Property Auctions with Teodor Bramwick

Podcast cover art 3000px by 3000px. Eye catching for a weekly podcast. The words should read Property Auctions (large font) with Teodor Bramwick (smaller font)

I would like the font and colours to be similar to my book, a copy of which I have attached.

Target Market(s)

New and experienced property investors looking to purchase at a property auction

```html
<!DOCTYPE html>
<html lang="en">
<head>
<meta charset="utf-8">
<title>Property Auctions with Teodor Bramwick</title>
<link rel="stylesheet" href="https://fonts.googleapis.com/css2?family=Oswald:wght@600&display=swap">
<style>
  :root {
    --navy-deep: #060a36;
    --navy-mid: #101c62;
    --navy-band: #0d1857;
    --gold-light: #fff38a;
    --gold-mid: #f1d64c;
    --gold-dark: #b48a1c;
  }
  html, body {
    margin: 0;
    padding: 0;
    width: 1200px;
    height: 1200px;
    overflow: hidden;
    background: var(--navy-deep);
  }
  .cover {
    position: relative;
    width: 1200px;
    height: 1200px;
    overflow: hidden;
    background: radial-gradient(ellipse at 50% 60%, var(--navy-mid) 0%, var(--navy-deep) 72%);
    font-family: "Oswald", "Arial Narrow", sans-serif;
  }
  .backdrop-pattern {
    position: absolute;
    left: 0;
    top: 497px;
    width: 1200px;
    height: 673px;
    background: linear-gradient(180deg, rgba(22, 35, 95, 0) 0%, var(--navy-band) 20%, var(--navy-band) 80%, rgba(22, 35, 95, 0) 100%);
  }
  .gold {
    background: linear-gradient(180deg, var(--gold-light) 0%, var(--gold-mid) 50%, var(--gold-dark) 100%);
    -webkit-background-clip: text;
    background-clip: text;
    color: transparent;
    filter: drop-shadow(0 6px 10px rgba(0, 0, 0, 0.55));
  }
  .title {
    position: absolute;
    left: 0;
    width: 1200px;
    margin: 0;
    text-align: center;
    font-weight: 600;
    font-size: 218px;
    line-height: 1;
    letter-spacing: -2px;
  }
  .title-line-1 { top: 52px; }
  .title-line-2 { top: 260px; }
  .emblem {
    position: absolute;
    left: 248px;
    top: 486px;
    width: 703px;
    height: 537px;
    border-radius: 28px;
    background: radial-gradient(ellipse at 50% 45%, var(--gold-light) 0%, var(--gold-mid) 40%, var(--gold-dark) 100%);
    box-shadow: 0 10px 24px rgba(0, 0, 0, 0.5);
  }
  .host {
    position: absolute;
    left: 0;
    top: 1057px;
    width: 1200px;
    margin: 0;
    text-align: center;
    font-weight: 600;
    font-size: 74px;
    line-height: 1;
  }
  .host .host-with {
    font-size: 48px;
    margin-right: 12px;
  }
</style>
</head>
<body>
  <main class="cover">
    <div class="backdrop-pattern" role="img" aria-label="Faint repeated FOR SALE and SOLD lettering pattern in dark blue"></div>

    <h1 class="title title-line-1 gold">PROPERTY</h1>
    <h1 class="title title-line-2 gold">AUCTIONS</h1>

    <div class="emblem" role="img" aria-label="Gold emblem: studio microphone under a house roof, flanked by pound signs and sound waves"></div>

    <p class="host gold"><span class="host-with">with</span>TEODOR BRAMWICK</p>
  </main>
</body>
</html>
```